KDR Business Card

Keystone Draper Resources is a successful and reputable financial services company.Our main services are home loans, commercial loans, vehicle finance and equipment finance. We also do development finance for property developers. Our company is always evolving to always be an industry leader in best financial service practices with access to the largest range of lenders in the country.

We want the business card to reflect our national finance company. Modern, professional corporate image. At the same time the concept of Keystone Draper Resources is that we help build wealth for you but the process for the client is an enjoyable peaceful experience. Not stressful at all .....

Colors to be same as the logo .... gold silver black white as the options

On the reverse side of the card I wanted either just the logo symbol or the logo symbol and text of the logo ....

It could be on a black background ..... or silver or gold .... want it to be quite striking to look at when you first see the card.

On the other side of the card I wanted the following details:

Martin Haldane
Director

0438 927 604

martin@kdrgrp.com.au

Po Box 718
Ferndale ACT 2614

www.kdrgrp.com.au

ACN 618 204 957 (This can be in very small print and can be in the bottom corner of the card or somewhere not very prominent)

As requested Ive uploaded the logo file in both .ai and .pdf formats. Please let me know if you need anything else. Thanks

Reason: Still deciding on which design I like best. I will provide individual feedback as well.

```html
<!DOCTYPE html>
<html lang="en">
<head>
<meta charset="utf-8">
<title>KDR Business Card</title>
<link rel="stylesheet" href="https://fonts.googleapis.com/css2?family=Marcellus+SC&family=Open+Sans:wght@400;600&display=swap">
<style>
  :root {
    --backdrop: #e8e5df;
    --gold-light: #fbf6df;
    --gold-mid: #eee1a8;
    --gold-deep: #c9a53f;
    --gold-text: #c8a33a;
    --silver-light: #fbfbfb;
    --silver-mid: #e6e6e8;
    --silver-deep: #c9c9cd;
    --ink: #2a2a2a;
    --ink-soft: #555555;
    --grey-text: #6e6e6e;
  }
  * { margin: 0; padding: 0; box-sizing: border-box; }
  html, body {
    width: 1200px;
    height: 1023px;
    overflow: hidden;
    background: var(--backdrop);
  }
  .canvas {
    position: relative;
    width: 1200px;
    height: 1023px;
  }
  .card {
    position: absolute;
    width: 560px;
    height: 320px;
    border-radius: 18px;
    overflow: hidden;
    box-shadow: 0 6px 18px rgba(0,0,0,0.12);
  }

  /* Front: contact side */
  .card--front {
    left: 320px;
    top: 150px;
    background: radial-gradient(ellipse at 50% 45%, var(--gold-light) 0%, #f6edc8 55%, var(--gold-mid) 100%);
  }
  .card__ornament {
    position: absolute;
    left: 120px;
    top: 22px;
    width: 320px;
    height: 276px;
    border-radius: 50%;
    background: radial-gradient(ellipse at center, rgba(255,255,255,0) 48%, rgba(214,178,78,0.55) 62%, rgba(214,178,78,0.15) 74%, rgba(255,255,255,0) 80%);
  }
  .contact {
    position: absolute;
    left: 0;
    right: 0;
    top: 82px;
    text-align: center;
    font-family: "Open Sans", sans-serif;
    color: var(--ink);
  }
  .contact__name {
    font-family: "Marcellus SC", serif;
    font-size: 27px;
    letter-spacing: 1px;
    color: var(--ink);
  }
  .contact__role {
    font-size: 10px;
    letter-spacing: 1.5px;
    text-transform: uppercase;
    color: var(--ink-soft);
    margin-top: 2px;
    margin-bottom: 14px;
  }
  .contact__line {
    font-size: 13px;
    line-height: 20px;
  }
  .card__acn {
    position: absolute;
    right: 18px;
    bottom: 14px;
    font-family: "Open Sans", sans-serif;
    font-size: 10px;
    color: var(--ink-soft);
    letter-spacing: 0.5px;
  }

  /* Back: brand side */
  .card--back {
    left: 320px;
    top: 560px;
    background: var(--silver-light);
  }
  .card__pattern {
    position: absolute;
    inset: 0;
    background: radial-gradient(ellipse at 45% 40%, var(--silver-light) 0%, var(--silver-mid) 70%, var(--silver-deep) 100%);
  }
  .brand {
    position: absolute;
    left: 0;
    right: 0;
    top: 118px;
    display: flex;
    align-items: center;
    justify-content: center;
    gap: 16px;
  }
  .brand__disc {
    width: 62px;
    height: 62px;
    border-radius: 50%;
    background: var(--gold-text);
  }
  .brand__name {
    font-family: "Marcellus SC", serif;
    font-size: 30px;
    letter-spacing: 1px;
    color: var(--gold-text);
  }
  .card__web {
    position: absolute;
    left: 22px;
    top: 50%;
    transform: translate(-50%, -50%) rotate(-90deg) translateY(0);
    transform-origin: center;
    font-family: "Open Sans", sans-serif;
    font-weight: 600;
    font-size: 12px;
    letter-spacing: 1px;
    color: var(--ink-soft);
    white-space: nowrap;
    margin-left: 12px;
  }
</style>
</head>
<body>
<main class="canvas">
  <section class="card card--front">
    <div class="card__ornament" role="img" aria-label="Gold sweeping ring ornament framing the contact details"></div>
    <div class="contact">
      <p class="contact__name">Martin Haldane</p>
      <p class="contact__role">Director</p>
      <p class="contact__line">0438 927 604</p>
      <p class="contact__line">martin@kdrgrp.com.au</p>
      <p class="contact__line">Po Box 718, Ferndale ACT 2614</p>
    </div>
    <p class="card__acn">ACN 618 204 957</p>
  </section>

  <section class="card card--back">
    <div class="card__pattern" role="img" aria-label="Faint silver floral background pattern"></div>
    <div class="brand">
      <span class="brand__disc"></span>
      <span class="brand__name">Keystone Draper Resources</span>
    </div>
    <p class="card__web">www.kdrgrp.com.au</p>
  </section>
</main>
</body>
</html>
```